Business Card Design Project

We need a business card design for a management consultancy focused on financial innovation and digital money, run by experts from the Financial Services, Telecoms and Money Transfer industries.
Our products include services such as Mobile Payments, Mobile Money, Digital Wallets, Online Payments, Branchless Banking and more. We work with regulatory information, business plans, financial modelling, strategic planning, new products functional specification, new technologies evaluation, etc.
See company logo attached.
We would like to see 2 versions: one in portuguese and one in english (regarding data information). You can see below information needed (whenever there is a difference between the two versions, the first one is in english and the second one in portuguese).

Name
Position
Phone/ Tel: ++61-2-xxxx-xxxx
Cell/ Cel: ++61-2-9 xxxx-xxxx
Dr. Tavares Lobato Av., 318 - Block C - 9th floor / Avenida Dr. Tavares Lobato, 318 - Torre II - 16o. andar
São Paulo - SP
01327-118 - Brazil/ 01327-118 - Brasil

Target Market(s)

Audience: C-level executives from banks, credit card companies, acquirers, IT developers, retailers

Industry/Entity Type

Financial

Requirements
Must have
• Must use the logo and information above. Front must have white background. Back side should have only logo.
Nice to have
• Back should be in another colour but if it seems too exxagerated, maintain back in white also.
Should not have
• Do not add other illustrations to the business card.

```html
<!DOCTYPE html>
<html lang="en">
<head>
<meta charset="utf-8">
<title>R Castellan Management Consulting – Business Card</title>
<link rel="stylesheet" href="https://fonts.googleapis.com/css2?family=Tinos:wght@400;700&display=swap">
<style>
  :root {
    --backdrop: #d0d0d0;
    --card-white: #ffffff;
    --card-black-center: #2a2a2c;
    --card-black-edge: #060606;
    --navy: #1d2668;
    --ink: #1a1a1a;
    --muted-ink: #333333;
    --logo-light: #c9ccd8;
    --rule: #111111;
  }
  * { box-sizing: border-box; margin: 0; padding: 0; }
  html, body {
    width: 1200px;
    height: 900px;
    overflow: hidden;
    background: var(--backdrop);
  }
  .canvas {
    position: relative;
    width: 1200px;
    height: 900px;
    font-family: "Tinos", "Times New Roman", serif;
  }
  .card {
    position: absolute;
    top: 300px;
    width: 520px;
    height: 300px;
    border-radius: 28px;
    overflow: hidden;
  }
  .card--back {
    left: 55px;
    background: radial-gradient(ellipse at 50% 45%, var(--card-black-center) 0%, var(--card-black-edge) 75%);
    display: flex;
    align-items: center;
    justify-content: center;
  }
  .card--front {
    left: 625px;
    background: var(--card-white);
  }
  .brand {
    display: flex;
    align-items: center;
    gap: 12px;
  }
  .brand__mark {
    width: 40px;
    height: 40px;
    flex: none;
  }
  .brand__name {
    font-weight: 400;
    text-transform: uppercase;
    line-height: 1.1;
  }
  .brand__line--main {
    display: block;
    font-size: 27px;
    letter-spacing: 1.5px;
  }
  .brand__line--sub {
    display: block;
    font-size: 15px;
    letter-spacing: 1px;
  }
  .card--back .brand__mark { background: var(--logo-light); }
  .card--back .brand__name { color: var(--logo-light); }
  .card--front .brand {
    position: absolute;
    left: 30px;
    top: 58px;
  }
  .card--front .brand__mark { background: var(--navy); }
  .card--front .brand__name { color: var(--navy); }
  .card__rule {
    position: absolute;
    left: 0;
    right: 0;
    top: 142px;
    height: 3px;
    background: var(--rule);
  }
  .holder {
    position: absolute;
    left: 32px;
    top: 158px;
  }
  .holder__name {
    font-size: 18px;
    color: var(--navy);
    font-weight: 400;
  }
  .holder__title {
    margin-top: 5px;
    font-size: 11px;
    color: var(--muted-ink);
  }
  .contacts {
    position: absolute;
    left: 32px;
    top: 212px;
    list-style: none;
    font-size: 12px;
    color: var(--ink);
    line-height: 14px;
  }
  .contacts__item {
    display: flex;
    align-items: flex-start;
    gap: 6px;
  }
  .contacts__icon {
    width: 12px;
    height: 12px;
    flex: none;
    margin-top: 1px;
    fill: var(--navy);
  }
  .contacts__indent { padding-left: 18px; }
</style>
</head>
<body>
<main class="canvas">

  <section class="card card--back" aria-label="Card back">
    <div class="brand">
      <span class="brand__mark"></span>
      <p class="brand__name"><span class="brand__line--main">R Castellan</span><span class="brand__line--sub">Management Consulting</span></p>
    </div>
  </section>

  <section class="card card--front" aria-label="Card front">
    <div class="brand">
      <span class="brand__mark"></span>
      <p class="brand__name"><span class="brand__line--main">R Castellan</span><span class="brand__line--sub">Management Consulting</span></p>
    </div>

    <div class="card__rule"></div>

    <div class="holder">
      <h1 class="holder__name">Dr. Tavares Lobato</h1>
      <p class="holder__title">Founder and Managing Partner</p>
    </div>

    <ul class="contacts">
      <li class="contacts__item">
        <svg class="contacts__icon" viewBox="0 0 24 24" aria-hidden="true"><path d="M6.6 10.8a15.1 15.1 0 0 0 6.6 6.6l2.2-2.2a1 1 0 0 1 1-.25 11.4 11.4 0 0 0 3.6.57 1 1 0 0 1 1 1V20a1 1 0 0 1-1 1A17 17 0 0 1 3 4a1 1 0 0 1 1-1h3.5a1 1 0 0 1 1 1c0 1.25.2 2.45.57 3.57a1 1 0 0 1-.25 1z"/></svg>
        <span>++61-2-xxxx-xxxx</span>
      </li>
      <li class="contacts__item">
        <svg class="contacts__icon" viewBox="0 0 24 24" aria-hidden="true"><path d="M7 1h10a2 2 0 0 1 2 2v18a2 2 0 0 1-2 2H7a2 2 0 0 1-2-2V3a2 2 0 0 1 2-2zm0 3v14h10V4zm5 15.5a1.2 1.2 0 1 0 0 2.4 1.2 1.2 0 0 0 0-2.4z"/></svg>
        <span>++61-2-9 xxxx-xxxx</span>
      </li>
      <li class="contacts__item">
        <svg class="contacts__icon" viewBox="0 0 24 24" aria-hidden="true"><path d="M2 5h20v14H2zm2 2v.5l8 5.5 8-5.5V7zm0 2.9V17h16V9.9l-8 5.5z"/></svg>
        <span>email@rcastellan.com</span>
      </li>
      <li class="contacts__item">
        <svg class="contacts__icon" viewBox="0 0 24 24" aria-hidden="true"><path d="M12 3 1 12h3v9h6v-6h4v6h6v-9h3z"/></svg>
        <span>Av., 318 - Block C - 9th floor</span>
      </li>
      <li class="contacts__item contacts__indent">
        <span>/ Avenida Dr. Tavares Lobato,</span>
      </li>
    </ul>
  </section>

</main>
</body>
</html>
```